Packaging design for a reclosable bag for our product

We have a logo, and we need to put it on packaging for our product and while we want the look to be simple, we want it to follow good design principles and also contain spaces for other product descriptions.

There will be 5 sizes at launch so I'd like 5 variations, one for each size.

I've included a few mockups of the type of bag that I made but they are all just rough ideas that I had.

I want the brand to look scientific and methodical and even a bit quirky, as in "wow this is a serious product but also a bit unusual."

```html
<!DOCTYPE html>
<html lang="en">
<head>
<meta charset="utf-8">
<title>VH2 Bias Lighting – Pouch Range</title>
<link rel="stylesheet" href="https://fonts.googleapis.com/css2?family=Mulish:wght@400;500;800;900&display=swap">
<style>
  :root {
    --page: #ffffff;
    --pouch: #1d1d1d;
    --pouch-spine: #272727;
    --seal: #141414;
    --seal-edge: #2e2e2e;
    --ink: #f2f2f2;
    --size-xl: #1592e6;
    --size-l: #f47b16;
    --size-m: #f5c400;
    --size-s: #8ad12a;
    --size-xs: #ec1c24;
  }
  * { box-sizing: border-box; margin: 0; padding: 0; }
  html, body { width: 1200px; height: 800px; overflow: hidden; background: var(--page); }
  body { font-family: "Mulish", "Helvetica Neue", Arial, sans-serif; }

  .range { position: relative; width: 1200px; height: 800px; }

  .pouch {
    position: absolute;
    width: 240px;
    height: 366px;
    background: var(--pouch);
    border-radius: 12px 12px 2px 2px;
    overflow: hidden;
    color: var(--ink);
  }
  .pouch::before {           /* side gusset band */
    content: "";
    position: absolute; left: 0; top: 0; bottom: 0; width: 40px;
    background: var(--pouch-spine);
  }
  .pouch::after {            /* zip seal line */
    content: "";
    position: absolute; left: 0; right: 0; top: 40px; height: 14px;
    background: var(--seal);
    border-top: 2px solid var(--seal-edge);
    border-bottom: 1px solid var(--seal-edge);
  }

  .pouch--xl { left: 76px;  top: 210px; z-index: 1; --accent: var(--size-xl); }
  .pouch--l  { left: 255px; top: 301px; z-index: 2; --accent: var(--size-l); }
  .pouch--m  { left: 496px; top: 145px; z-index: 1; --accent: var(--size-m); }
  .pouch--s  { left: 696px; top: 229px; z-index: 1; --accent: var(--size-s); }
  .pouch--xs { left: 898px; top: 305px; z-index: 2; --accent: var(--size-xs); }

  .label { position: absolute; left: 0; top: 196px; width: 100%; z-index: 1; }

  .brand {
    position: absolute; left: 48px; top: 0;
    font-weight: 800; font-size: 36px; line-height: 1; letter-spacing: -1.5px;
    color: var(--ink);
  }
  .size-tag {
    position: absolute; left: 2px; top: 46px;
    width: 39px; height: 38px;
    background: var(--accent);
    color: #fff;
    font-weight: 900; font-size: 18px;
    display: flex; align-items: center; justify-content: center;
    letter-spacing: -0.5px;
  }
  .product {
    position: absolute; left: 48px; top: 48px;
    font-weight: 500; font-size: 17px; letter-spacing: 0.3px;
  }
  .length {
    position: absolute; left: 48px; top: 71px;
    font-weight: 500; font-size: 10px; letter-spacing: 0.3px;
    color: var(--accent);
  }
  .spec {
    position: absolute; left: 48px; top: 94px;
    font-weight: 400; font-size: 11px; line-height: 14px; letter-spacing: 0.2px;
  }
  .spec span { display: block; }
  .spec span + span { font-size: 10px; }
</style>
</head>
<body>
<main class="range">

  <article class="pouch pouch--xl">
    <div class="label">
      <p class="brand">VH2</p>
      <p class="size-tag">XL</p>
      <h2 class="product">Bias Lighting</h2>
      <p class="length">5 Meters / 16.4 Feet</p>
      <p class="spec"><span>Simulated D65 CRI 90+</span><span>6500K White Bias Lighting</span></p>
    </div>
  </article>

  <article class="pouch pouch--l">
    <div class="label">
      <p class="brand">VH2</p>
      <p class="size-tag">L</p>
      <h2 class="product">Bias Lighting</h2>
      <p class="length">4 Meters / 13.1 Feet</p>
      <p class="spec"><span>Simulated D65 CRI 90+</span><span>6500K White Bias Lighting</span></p>
    </div>
  </article>

  <article class="pouch pouch--m">
    <div class="label">
      <p class="brand">VH2</p>
      <p class="size-tag">M</p>
      <h2 class="product">Bias Lighting</h2>
      <p class="length">3 Meters / 9.8 Feet</p>
      <p class="spec"><span>Simulated D65 CRI 90+</span><span>6500K White Bias Lighting</span></p>
    </div>
  </article>

  <article class="pouch pouch--s">
    <div class="label">
      <p class="brand">VH2</p>
      <p class="size-tag">S</p>
      <h2 class="product">Bias Lighting</h2>
      <p class="length">2 Meters / 6.6 Feet</p>
      <p class="spec"><span>Simulated D65 CRI 90+</span><span>6500K White Bias Lighting</span></p>
    </div>
  </article>

  <article class="pouch pouch--xs">
    <div class="label">
      <p class="brand">VH2</p>
      <p class="size-tag">XS</p>
      <h2 class="product">Bias Lighting</h2>
      <p class="length">1 Meter / 3.3 Feet</p>
      <p class="spec"><span>Simulated D65 CRI 90+</span><span>6500K White Bias Lighting</span></p>
    </div>
  </article>

</main>
</body>
</html>
```